Business Card Design

I am a cosmetic tattooist in Melbourne Australia, who provides services where by I tattoo eyebrows in block or strokes with a tattooing gun. Feathering that mimic hair strands with a scalpel. Eyeliner top and bottom with the tattooing gun. Lips just as either an outline or a full block colour where the top and bottom lip is completely covered. Corrections for tattooing done previously that have either faded to quickly, turned blue or orange due to bad colour choice, or a mishap. Paramedical colouring for people who either have scaring that needs to be matched to their skin colour. Patients who have alopecia or a skin condition that needs hair like tattooing. Cancer patients who's nipples and areolas have been partially or totally been removed and require them to be re drawn into the new skin. I colour match with a variety of inks (around 50) at my disposal and can also lift colours with a pigmentation lifter. I also require the use of two different types of anaesthetics throughout each procedure.
Colours that I have looked into the represent health, professionalism, beauty, skin and medical type procedures are Light to dark brown, Light to dark grey, Black and White. Possibly a splash of red to represent the lips. I am mobile and can work from any venue that takes a commission for a bed. I have completed a diploma in cosmetic tattooing being qualified.
Updates

Project Deadline Extended
Reason: I have been awaiting for a design from own more designer who accepted my project but hasn't released their design.

Project Deadline Extended

Industry/Entity Type

Medical

Contact Information for Business Card

Company name: Velvet Arch Cosmetic Tattooing
Name: Lorna Beswick
Title: Cosmetic and Paramedical Tattooist
Address: P.O Box 2863, Ashmont Heights, Victoria 3297
Mobile: 0417365821
Email: velvetarchtattooing@quillmail.example
Preferred colours: Light brown, Light Grey, Black (writing) White Background

Requirements
Nice to have
• A shape of the eyebrow or eye with eyeliner in the background. Possibly red lips. No straight lines, only curved or curled lines.

```html
<!DOCTYPE html>
<html lang="en">
<head>
<meta charset="utf-8">
<title>Velvet Arch Cosmetic Tattooing – Business Card</title>
<link rel="stylesheet" href="https://fonts.googleapis.com/css2?family=Dancing+Script:wght@600&family=Questrial&display=swap">
<style>
  :root {
    --ink: #111111;
    --paper: #ffffff;
    --skin-deep: #e4a897;
    --skin-mid: #f0c6b6;
    --skin-light: #f8e3da;
  }
  html, body {
    margin: 0;
    padding: 0;
    width: 1200px;
    height: 741px;
    overflow: hidden;
    background: var(--paper);
  }
  .card {
    position: relative;
    width: 1200px;
    height: 741px;
    overflow: hidden;
    background: var(--paper);
    color: var(--ink);
  }
  .portrait-area {
    position: absolute;
    inset: 0;
    width: 1200px;
    height: 741px;
  }
  .brand {
    position: absolute;
    left: 66px;
    top: 66px;
    margin: 0;
    font-family: "Dancing Script", cursive;
    font-weight: 600;
    font-size: 96px;
    line-height: 92px;
    color: var(--ink);
  }
  .brand span { display: block; }
  .brand .line-two { margin-left: 8px; }
  .identity {
    position: absolute;
    right: 60px;
    top: 312px;
    text-align: right;
    font-family: "Questrial", sans-serif;
  }
  .person-name {
    margin: 0;
    font-size: 53px;
    font-weight: 400;
    letter-spacing: 1px;
    line-height: 60px;
  }
  .person-role {
    margin: 0;
    font-size: 33px;
    line-height: 40px;
  }
  .contact {
    position: absolute;
    right: 58px;
    top: 452px;
    margin: 0;
    padding: 0;
    list-style: none;
    font-family: "Questrial", sans-serif;
    font-size: 33px;
    line-height: 46px;
    text-align: right;
  }
  .contact li {
    display: flex;
    justify-content: flex-end;
    align-items: flex-start;
    gap: 12px;
    margin-bottom: 16px;
  }
  .contact .text { display: block; }
  .contact .icon {
    width: 42px;
    height: 42px;
    flex: none;
    margin-top: 2px;
  }
  .contact .address .text { margin-right: 0; }
  .contact .address .second { margin-right: 54px; display: block; }
</style>
</head>
<body>
<main class="card">
  <svg class="portrait-area" role="img" aria-label="Close-up photograph of an eye with tattooed eyeliner, lashes and brow, in soft skin tones" viewBox="0 0 1200 741" xmlns="http://www.w3.org/2000/svg">
    <defs>
      <radialGradient id="skin-glow" cx="220" cy="640" r="820" gradientUnits="userSpaceOnUse">
        <stop offset="0" stop-color="var(--skin-deep)"/>
        <stop offset="0.35" stop-color="var(--skin-mid)"/>
        <stop offset="0.62" stop-color="var(--skin-light)"/>
        <stop offset="0.85" stop-color="var(--paper)"/>
      </radialGradient>
    </defs>
    <rect width="1200" height="741" fill="url(#skin-glow)"/>
  </svg>

  <h1 class="brand">
    <span class="line-one">Velvet Arch Cosmetic</span>
    <span class="line-two">Tattooing</span>
  </h1>

  <div class="identity">
    <p class="person-name">LORNA BESWICK</p>
    <p class="person-role">Cosmetic and Paramedical Tattooist</p>
  </div>

  <ul class="contact">
    <li class="address">
      <span class="text">P.O Box 2863, Ashmont Heights,<span class="second">Victoria 3297</span></span>
      <svg class="icon" viewBox="0 0 42 42" aria-hidden="true">
        <path d="M21 4 L3 20 L8 20 L8 36 L17 36 L17 26 L25 26 L25 36 L34 36 L34 20 L39 20 Z" fill="var(--ink)"/>
      </svg>
    </li>
    <li class="phone">
      <span class="text">0417365821</span>
      <svg class="icon" viewBox="0 0 42 42" aria-hidden="true">
        <rect x="11" y="8" width="20" height="32" rx="3" fill="var(--ink)"/>
        <rect x="14" y="0" width="3" height="9" fill="var(--ink)"/>
        <rect x="14" y="12" width="14" height="9" fill="var(--paper)"/>
        <g fill="var(--paper)">
          <rect x="14" y="24" width="3" height="2"/><rect x="19.5" y="24" width="3" height="2"/><rect x="25" y="24" width="3" height="2"/>
          <rect x="14" y="29" width="3" height="2"/><rect x="19.5" y="29" width="3" height="2"/><rect x="25" y="29" width="3" height="2"/>
          <rect x="14" y="34" width="3" height="2"/><rect x="19.5" y="34" width="3" height="2"/><rect x="25" y="34" width="3" height="2"/>
        </g>
      </svg>
    </li>
    <li class="email">
      <span class="text">velvetarchtattooing@quillmail.example</span>
      <svg class="icon" viewBox="0 0 42 42" aria-hidden="true">
        <rect x="3" y="3" width="36" height="36" rx="5" fill="var(--ink)"/>
        <path d="M9 18 L21 10 L33 18 L33 33 L9 33 Z" fill="none" stroke="var(--paper)" stroke-width="2"/>
        <path d="M9 18 L21 27 L33 18" fill="none" stroke="var(--paper)" stroke-width="2"/>
        <circle cx="21" cy="18" r="3" fill="none" stroke="var(--paper)" stroke-width="1.6"/>
      </svg>
    </li>
  </ul>
</main>
</body>
</html>
```